Business Cards for Lean-In-Wise

I need a business card that uses elements of my color pallet and book along with my company name and logo. The primary thing I'd like to have stand out is the word Lean-In-Wise (i'd like to see this word in the orange from my pallet)
On the back of the card I want it to say Stop being Accountable, Be Lean-In-Wise

Contact Information for Business Card

Summit Hearthgroup logo, Lean-In-Wise, email - rtm@summithearthgroup.example, phone 555-208-4917, Los Angeles | Toronto

Requirements
Nice to have
• colors from my color pallet

```html
<!DOCTYPE html>
<html lang="en">
<head>
<meta charset="utf-8">
<title>Lean-In-Wise Business Card</title>
<link href="https://fonts.googleapis.com/css2?family=Oswald:wght@600;700&family=Montserrat:wght@400;700&family=Roboto:wght@400&display=swap" rel="stylesheet">
<style>
  :root {
    --page-bg: #e9e6e1;
    --card-white: #ffffff;
    --card-black: #0a0a0a;
    --brand-orange: #ef5a23;
    --brand-blue: #1d5fbf;
    --brand-navy: #0d3f9e;
    --ink: #1e1e1e;
  }
  * { margin: 0; padding: 0; box-sizing: border-box; }
  html, body { width: 1200px; height: 900px; overflow: hidden; }
  body {
    background: var(--page-bg);
    position: relative;
    font-family: "Roboto", Arial, sans-serif;
  }
  .card {
    position: absolute;
    left: 250px;
    width: 700px;
    height: 400px;
    border-radius: 26px;
    box-shadow: 0 10px 28px rgba(0,0,0,0.22);
    overflow: hidden;
  }
  /* Back of card */
  .card-back {
    top: 40px;
    background: var(--card-black);
  }
  .back-slogan {
    position: absolute;
    left: 70px;
    top: 120px;
    font-family: "Oswald", "Arial Narrow", sans-serif;
    font-weight: 700;
    color: var(--brand-orange);
    text-transform: uppercase;
    line-height: 1.05;
  }
  .back-slogan .line-small { display: block; font-size: 44px; }
  .back-slogan .line-large { display: block; font-size: 76px; }

  /* Front of card */
  .card-front {
    top: 460px;
    background: var(--card-white);
  }
  .front-headline {
    position: absolute;
    left: 50px;
    top: 72px;
    font-family: "Oswald", "Arial Narrow", sans-serif;
    font-weight: 700;
    font-size: 60px;
    line-height: 1;
    color: var(--brand-orange);
    text-transform: uppercase;
    letter-spacing: 0.5px;
  }
  .brand-mark {
    position: absolute;
    right: 50px;
    top: 34px;
    width: 190px;
    display: flex;
    flex-direction: column;
    align-items: center;
    gap: 10px;
  }
  .brand-dot {
    width: 40px; height: 40px;
    border-radius: 50%;
    background: var(--brand-blue);
  }
  .brand-name {
    font-family: "Montserrat", Arial, sans-serif;
    font-weight: 400;
    font-size: 24px;
    line-height: 1.15;
    text-align: center;
    color: var(--brand-blue);
  }
  .locations {
    position: absolute;
    left: 58px;
    top: 185px;
    list-style: none;
    font-size: 20px;
    color: var(--ink);
    line-height: 1.3;
  }
  .locations li::before {
    content: "";
    display: inline-block;
    width: 9px; height: 9px;
    border-radius: 50%;
    background: var(--brand-navy);
    margin-right: 10px;
    vertical-align: middle;
  }
  .contact-list {
    position: absolute;
    left: 58px;
    top: 270px;
    list-style: none;
    font-size: 19px;
    color: var(--ink);
    line-height: 1.45;
  }
  .contact-list li { display: flex; align-items: center; gap: 14px; }
  .contact-list svg { width: 18px; height: 18px; flex: none; }
  .contact-list .web-domain { color: var(--brand-blue); }
  .person {
    position: absolute;
    right: 50px;
    top: 212px;
    text-align: right;
  }
  .person-name {
    font-family: "Montserrat", Arial, sans-serif;
    font-weight: 700;
    font-size: 26px;
    color: var(--brand-navy);
    text-transform: uppercase;
  }
  .person-title {
    font-size: 20px;
    color: var(--ink);
    margin-top: 4px;
  }
</style>
</head>
<body>

  <section class="card card-back" aria-label="Card back">
    <h2 class="back-slogan">
      <span class="line-small">Stop being Accountable,</span>
      <span class="line-large">Be Lean-In-Wise</span>
    </h2>
  </section>

  <section class="card card-front" aria-label="Card front">
    <h1 class="front-headline">Lean-In-Wise</h1>

    <div class="brand-mark">
      <span class="brand-dot"></span>
      <span class="brand-name">Summit<br>Hearthgroup</span>
    </div>

    <ul class="locations">
      <li>Los Angeles</li>
      <li>Toronto</li>
    </ul>

    <ul class="contact-list">
      <li>
        <svg viewBox="0 0 24 24" aria-hidden="true"><path fill="#0d3f9e" d="M6.6 10.8a15 15 0 0 0 6.6 6.6l2.2-2.2c.3-.3.7-.4 1-.2 1.1.4 2.3.6 3.6.6.6 0 1 .4 1 1V20c0 .6-.4 1-1 1A17 17 0 0 1 3 4c0-.6.4-1 1-1h3.5c.6 0 1 .4 1 1 0 1.3.2 2.5.6 3.6.1.3 0 .7-.2 1z"/></svg>
        <span>555-208-4917</span>
      </li>
      <li>
        <svg viewBox="0 0 24 24" aria-hidden="true"><rect x="3" y="5" width="18" height="14" rx="1.5" fill="none" stroke="#0d3f9e" stroke-width="2"/><path d="M3.5 6l8.5 7 8.5-7" fill="none" stroke="#0d3f9e" stroke-width="2"/></svg>
        <span>rtm@summithearthgroup.example</span>
      </li>
      <li>
        <svg viewBox="0 0 24 24" aria-hidden="true"><circle cx="12" cy="12" r="9" fill="none" stroke="#0d3f9e" stroke-width="2"/><ellipse cx="12" cy="12" rx="4" ry="9" fill="none" stroke="#0d3f9e" stroke-width="1.6"/><path d="M3 12h18M5 7.5h14M5 16.5h14" stroke="#0d3f9e" stroke-width="1.4"/></svg>
        <span>www.<span class="web-domain">summithearthgroup.example</span></span>
      </li>
    </ul>

    <div class="person">
      <p class="person-name">Dana Whitfield</p>
      <p class="person-title">Director</p>
    </div>
  </section>

</body>
</html>
```